Business Card and Letterhead Design for Public Accounting Firm

Business card and letterhead design for a CPA Firm located in Orange County, CA. We're looking for a modern and professional design utilizing our existing logo. We'd like a clean "less is more" look, but also something that catches the eye. We provide a high level of service to our clients. Open to single or double sided business cards.

Additional info: color numbers on logo
Blue :
R 0
G 83
B 125

#00537D

Silver :

R 154
G 154
B 154

#9A9A9A

Target Market(s)

Businesses and individuals

Industry/Entity Type

Accounting

Contact Information for Business Card

Moss Whitfield & Danby LLP - 4827 Larkspur Vale Road, Irvine, CA 92614 - (949)731-2864 - mwdaccts.example

Font styles to use
Serif
Sans Serif
Other font styles liked:
• See font file uploaded

Colors
0054AA
0677BA
7BADD7
CADEEF
E8F1F8

Requirements
Nice to have
• Possibly use the font file provided which matches our logo, but adjust to be not in all caps

```html
<!DOCTYPE html>
<html lang="en">
<head>
<meta charset="utf-8">
<title>Moss Whitfield &amp; Danby LLP — Business Card</title>
<link href="https://fonts.googleapis.com/css2?family=PT+Serif:wght@400&display=swap" rel="stylesheet">
<style>
  :root {
    --stage: #2a2a2a;
    --paper: #f1f1f0;
    --blue: #1c4a73;
    --silver: #9a9a9a;
    --ink-grey: #868686;
    --text-grey: #6e6e6e;
    --white: #ffffff;
  }
  * { box-sizing: border-box; margin: 0; padding: 0; }
  html, body { width: 1200px; height: 1138px; overflow: hidden; }
  body {
    background: var(--stage);
    font-family: "PT Serif", Georgia, serif;
    position: relative;
  }
  .card {
    position: absolute;
    left: 275px;
    width: 622px;
    height: 376px;
    background: var(--paper);
    border-radius: 12px;
    overflow: hidden;
  }
  .card--front { top: 185px; }
  .card--back { top: 607px; }

  .firm-name {
    color: var(--ink-grey);
    text-transform: uppercase;
    letter-spacing: 0.14em;
    line-height: 1.18;
    font-weight: 400;
  }
  .card--front .firm-name {
    position: absolute;
    left: 0; right: 0;
    top: 143px;
    text-align: center;
    font-size: 29px;
  }
  .website-line {
    position: absolute;
    left: 0; right: 0;
    top: 320px;
    text-align: center;
    font-size: 15px;
    letter-spacing: 0.95em;
    color: var(--blue);
  }
  .accent-band {
    position: absolute;
    left: 0; right: 0; bottom: 0;
    height: 14px;
    display: flex;
  }
  .accent-band__blue { flex: 1; background: var(--blue); }
  .accent-band__silver { flex: 1; background: var(--silver); }

  .card--back .firm-name {
    position: absolute;
    left: 44px;
    top: 46px;
    font-size: 26px;
  }
  .person-name {
    position: absolute;
    left: 45px;
    top: 143px;
    font-size: 30px;
    color: var(--blue);
    font-weight: 400;
  }
  .contact {
    position: absolute;
    left: 44px;
    top: 190px;
    font-size: 15.5px;
    color: var(--text-grey);
    line-height: 23.5px;
    list-style: none;
  }
  .contact li { display: flex; align-items: flex-start; }
  .contact__icon {
    width: 14px; height: 14px;
    margin: 4px 14px 0 0;
    flex: none;
    fill: var(--blue);
  }
  .contact__pair { display: flex; gap: 18px; }
  .contact__pair span { display: flex; }
  .waves { position: absolute; left: 0; top: 0; }
  .tagline {
    position: absolute;
    right: 50px;
    top: 295px;
    text-align: right;
    font-size: 17px;
    line-height: 24px;
    color: var(--white);
  }
</style>
</head>
<body>

<section class="card card--front" aria-label="Business card front">
  <h1 class="firm-name">Moss Whitfield<br>&amp; Danby LLP</h1>
  <p class="website-line">www.mwdaccts.example</p>
  <div class="accent-band"><span class="accent-band__blue"></span><span class="accent-band__silver"></span></div>
</section>

<section class="card card--back" aria-label="Business card back">
  <svg class="waves" width="622" height="376" viewBox="0 0 622 376" aria-hidden="true">
    <path fill="#a3a3a3" d="M0,296 C110,360 300,372 420,286 C500,232 560,228 622,238 L622,254 C540,248 472,262 404,300 C300,360 130,356 0,316 Z"/>
    <path fill="#1c4a73" d="M0,333 C120,382 280,382 404,314 C474,276 540,256 622,262 L622,376 L0,376 Z"/>
  </svg>

  <h2 class="firm-name">Moss Whitfield<br>&amp; Danby LLP</h2>
  <p class="person-name">Evan Holloway</p>

  <ul class="contact">
    <li class="contact__pair">
      <span>
        <svg class="contact__icon" viewBox="0 0 16 16" aria-hidden="true"><path d="M1 5c0-2 3-3 7-3s7 1 7 3v1h-3V5H4v1H1zM4 7h8l2 7H2zM8 9a2 2 0 100 4 2 2 0 000-4z"/></svg>
        (949)731-2864
      </span>
      <span>
        <svg class="contact__icon" viewBox="0 0 16 16" aria-hidden="true"><path d="M1 3h14v10H1zM2 4l6 5 6-5v1.5L8 10.5 2 5.5z" fill-rule="evenodd"/></svg>
        evan@mwdaccts.example
      </span>
    </li>
    <li>
      <svg class="contact__icon" viewBox="0 0 16 16" aria-hidden="true"><path d="M8 0a6 6 0 00-6 6c0 4 6 10 6 10s6-6 6-10a6 6 0 00-6-6zm0 3.5a2.5 2.5 0 110 5 2.5 2.5 0 010-5z" fill-rule="evenodd"/></svg>
      <span>4827 Larkspur Vale Road,<br>Irvine, CA 92614</span>
    </li>
    <li>
      <svg class="contact__icon" viewBox="0 0 16 16" aria-hidden="true"><circle cx="8" cy="8" r="7"/><path d="M1 8h14M8 1c-3 3-3 11 0 14M8 1c3 3 3 11 0 14M2.5 4.5h11M2.5 11.5h11" stroke="#f1f1f0" stroke-width="1" fill="none"/></svg>
      www.mwdaccts.example
    </li>
  </ul>

  <p class="tagline">Certified<br>Public Accountants</p>
</section>

</body>
</html>
```